Web Design Project

I'm looking for a web design that incorporates the content included below into a web site that is clearly for a platform as a service product that helps people build complex web information systems that also do mobile apps and integrations.
Updates

Project Deadline Extended
Reason: I would like to encourage more submissions so I'm extending the deadline. Designs submitted earlier may win due to immediate need for some collateral. We will be posting several other contests in the near future if this one goes well.

Here are some sample web sites we like quite a lot:

http://www.plovra.com
http://www.zenthark.com/
http://www.zenthark.com/skyvault/ipaas-cloud-based-integration-demand
http://www.quorvelnet.com/hybrid-it

It is really important that the first 5 graphic panels in the word document get translated into a rotating banner for the home page.

Our software integrates databases, services, social-media, security, and mobile devices, but it starts with building great web applications for the desktop and real integrated systems for businesses. We also integrate accounting, CRM, and lots of other things together - that's important.

We focus on creating one system. Please try to capture that concept. Don't deliver just mobile - we're system first, and mobile second. The goal is to help our customers merge all their systems into one.

Target Market(s)

CIOs, CTOs, Technical Decision Makers, Business People

Industry/Entity Type

Build

Requirements
Must have
• Home Page that introduces the product and what it can do for people. Product Page that shows options for the product: Platform as a Service and Licensing. Services page that shows options for Services - Virtual Development Teams and Professional Services. A Blog Page. About Us Page with location info, contact info, etc.
Nice to have
• Scrolling home page banners. Lead generation - Contact us form.

```html
<!DOCTYPE html>
<html lang="en">
<head>
<meta charset="utf-8">
<title>Emberlift – Custom enterprise software</title>
<link href="https://fonts.googleapis.com/css2?family=Oswald:wght@400;500&family=Arimo:wght@400;700&display=swap" rel="stylesheet">
<style>
:root{
  --blue:#0a5fa8;
  --blue-light:#1a8fd6;
  --navy:#064a8a;
  --navy-deep:#043a70;
  --red:#d4141c;
  --orange:#e68a12;
  --gold-top:#fde39a;
  --gold-bot:#f6b94a;
  --text:#444;
  --muted:#666;
  --line:#d8e3ec;
  --row-blue:#b9d8ee;
  --row-gold:#f3b95c;
  --row-orange:#e19443;
}
*{box-sizing:border-box;margin:0;padding:0}
html,body{width:987px;height:1200px;overflow:hidden}
body{position:relative;background:#fff;font-family:"Arimo",Arial,sans-serif;color:var(--text)}
.abs{position:absolute}

/* header */
.site-header{left:0;top:0;width:987px;height:133px;background:linear-gradient(#fff7e0,#fff 60%)}
.brand{left:109px;top:16px;display:flex;align-items:center;gap:10px}
.brand-mark{width:52px;height:52px;border-radius:50%;background:var(--orange)}
.brand-name{font-family:"Oswald",sans-serif;font-weight:500;font-size:32px;color:var(--blue);line-height:1}
.tagline{left:191px;top:62px;font-family:"Oswald",sans-serif;font-size:14px;color:#222}
.call{right:110px;top:62px;font-family:"Oswald",sans-serif;font-size:14px;color:#222}
.call b{color:var(--red);font-weight:400}

.main-nav{left:108px;top:98px;width:771px;height:33px;border:1px solid #ccc;border-radius:3px;background:linear-gradient(#fff,#e6e6e6)}
.main-nav ul{list-style:none;display:flex;height:100%;align-items:center;padding-left:6px}
.main-nav li{font-family:"Oswald",sans-serif;font-size:13px;color:#222;padding:0 15px;border-right:1px solid #ccc;line-height:16px}
.main-nav li:last-child{border:none}
.main-nav li.active{background:linear-gradient(var(--blue-light),var(--navy));color:#fff;border:none;height:42px;margin-top:-8px;line-height:42px;border-radius:3px 3px 0 0;margin-left:-1px}
.search{right:36px;top:5px;width:134px;height:22px;border:1px solid #aaa;background:#fff;font-size:10px;color:#999;padding:4px 6px}
.search-btn{right:10px;top:5px;width:26px;height:22px;background:var(--navy)}

/* hero */
.hero{left:0;top:133px;width:987px;height:297px;background:radial-gradient(ellipse at 50% 40%,#fff 0%,#e6f3fc 45%,#9fd1f2 100%)}
.hero h2{width:100%;text-align:center;font-family:"Oswald",sans-serif;font-weight:400}
.hero .kicker{top:12px;font-size:19px;color:var(--blue-light)}
.hero .headline{top:36px;font-size:26px;color:var(--red)}
.hero-art{left:130px;top:82px;width:697px;height:178px;border-radius:6px;background:linear-gradient(90deg,#cfd6dd,#f4e2b8 45%,#2a3340 75%,#3a4452)}
.dots{top:280px;left:474px;display:flex;gap:5px}
.dots i{width:10px;height:10px;border-radius:50%;border:2px solid #fff;background:#d7e8f5}
.dots i.on{background:var(--blue)}

/* intro */
.intro{top:452px;width:987px;text-align:center;font-family:"Oswald",sans-serif;font-weight:400;font-size:18px;color:var(--orange)}
.stat{top:493px;width:248px;height:46px;border-radius:2px;display:flex;align-items:center;justify-content:center;font-size:13px;color:#222;background:linear-gradient(var(--gold-top),var(--gold-bot));border:1px solid #e7a53a}
.stat.blue{background:linear-gradient(#1f7ac4,var(--navy-deep));border-color:var(--navy-deep);color:#fff}

.section-title{width:987px;text-align:center;font-size:22px;font-weight:700;color:var(--blue)}
.section-sub{top:597px;width:987px;text-align:center;font-size:11.5px;color:var(--muted)}

.grid{left:108px;width:771px;display:grid;grid-template-columns:repeat(3,1fr);border:1px solid var(--line);overflow:hidden}
.grid .head{height:26px;padding:6px 10px;font-size:12.5px;color:#222;border-right:1px solid rgba(255,255,255,.6)}
.grid .body{height:47px;padding:9px 8px 0 10px;font-size:9.8px;letter-spacing:-0.1px;line-height:14px;color:var(--muted);border-right:1px solid var(--line);overflow:hidden}
.grid .body.tall{height:50px}
.grid .head.blue{background:var(--row-blue)}
.grid .head.gold{background:var(--row-gold)}
.grid .head.orange{background:var(--row-orange)}

/* footer */
.site-footer{left:0;top:934px;width:987px;height:266px;background:linear-gradient(var(--blue),var(--navy-deep));color:#fff}
.footer-col h3{font-size:20px;font-weight:700}
.news{left:108px;top:16px;width:255px}
.news h4{font-size:11px;font-weight:400;margin-top:10px}
.news time{display:block;font-size:9px;color:#b8d4ec;margin:4px 0 8px}
.news p{font-size:10px;line-height:14px}
.news a{color:#fff;font-weight:700}
.center{left:363px;top:0;width:250px;height:220px;border-left:1px solid rgba(255,255,255,.12);border-right:1px solid rgba(255,255,255,.12);padding:12px 14px}
.center .brand{position:static}
.center .brand-name{color:#fff;font-size:32px}
.center .brand-mark{width:48px;height:48px}
.info{display:flex;gap:10px;align-items:flex-start;font-size:10.5px;line-height:15px;margin-top:10px;padding-left:54px;white-space:nowrap}
.info svg{flex:none;margin-top:1px}
.socials{display:flex;gap:10px;margin:16px 0 0 54px}
.socials span{width:32px;height:32px;border-radius:4px;background:#3d82c4;border:2px solid #fff}
.contact{left:632px;top:16px;width:247px}
.field{height:26px;border:1px solid #2c7fc4;background:var(--navy-deep);font-size:10px;color:#9cbddb;padding:7px 7px}
.row2{display:grid;grid-template-columns:1fr 1fr;gap:10px;margin-top:10px}
.msg{height:58px;margin-top:10px}
.submit{float:right;margin-top:12px;width:58px;height:24px;background:linear-gradient(var(--gold-top),var(--gold-bot));color:#222;font-size:11px;display:flex;align-items:center;justify-content:center;border-radius:2px}
.footer-bar{left:0;top:220px;width:987px;height:46px;border-top:1px solid rgba(255,255,255,.15);font-size:10px;color:#d8e6f3}
.footer-bar .links{left:108px;top:20px}
.footer-bar .copy{right:108px;top:20px}
</style>
</head>
<body>

<header class="site-header abs">
  <div class="brand abs"><span class="brand-mark"></span><span class="brand-name">Emberlift</span></div>
  <p class="tagline abs">Custom enterprise software at the speed of thought</p>
  <p class="call abs"><b>Call Today:</b> +155 501 0199</p>
  <nav class="main-nav abs">
    <ul>
      <li>HOME</li><li class="active">PLATFORM</li><li>SERVICES</li><li>BLOG</li><li>ABOUT US</li>
    </ul>
    <div class="search abs">Enter Your Search Items</div>
    <div class="search-btn abs">
      <svg width="26" height="22" viewBox="0 0 26 22"><circle cx="12" cy="10" r="5" fill="none" stroke="#fff" stroke-width="2"/><line x1="15.5" y1="13.5" x2="19" y2="17" stroke="#fff" stroke-width="2"/></svg>
    </div>
  </nav>
</header>

<section class="hero abs">
  <h2 class="kicker abs">CREATE CUSTOM ENTERPRISE SOFTWARE</h2>
  <h2 class="headline abs">WHERE YOU NEED IT CONNECTING CUSTOMERS AND PARTNERS TO YOU</h2>
  <div class="hero-art abs" role="img" aria-label="Laptop, cloud of app icons, smartphone and tablet showing the platform's software"></div>
  <div class="dots abs"><i class="on"></i><i></i><i></i></div>
</section>

<h2 class="intro abs">INTRODUCING THE EMBERLIFT PLATFORM™ . THE POWER OF OFF-THE-SHELF, THE CAPABILITY TO DO-IT-YOURSELF.</h2>
<div class="stat abs" style="left:108px">Emberlift Platform Launched -&nbsp;<b>July 2012</b></div>
<div class="stat blue abs" style="left:370px">Revenue $1m in 2012, $2m+&nbsp;<b>in 2013</b></div>
<div class="stat abs" style="left:632px"><b>$250k</b>&nbsp;Project to Expand Market</div>

<h2 class="section-title abs" style="top:566px">Save Time and Money</h2>
<p class="section-sub abs">The Emberlift Platform™ reduces the time and effort it requires to deliver enterprise software without compromising your process.</p>

<div class="grid abs" style="top:623px">
  <div class="head blue">Do More with Less</div><div class="head blue">Improve Quality</div><div class="head blue">Future Proof</div>
  <div class="body tall">Deliver custom software and services with 80% less work and better visibility.</div>
  <div class="body tall">Eliminatedefects on software that has nothing to do with your business.</div>
  <div class="body tall">Upgrade to the latest technology in a fraction of the time and save.</div>
</div>

<h2 class="section-title abs" style="top:722px">Quickly Solve Serious Problems in a New Way</h2>

<div class="grid abs" style="top:757px">
  <div class="head gold">Invent</div><div class="head gold">Re-Imagine</div><div class="head gold">Integrate &amp; Secure</div>
  <div class="body">Translate concepts into working systems you can touch with white-box software creation.</div>
  <div class="body">Refresh legacy systems. Let Emberlift auto-discover and create working software you can use right away.</div>
  <div class="body">Fill gaps and createconnectionsin record time. Secure apps and information from one place.</div>
</div>

<div class="grid abs" style="top:842px">
  <div class="head orange">Mobilize</div><div class="head orange">Coordinate</div><div class="head orange">Consolidate</div>
  <div class="body">Create mobile and tablet apps that work just like your desktop systems. Do your work from anywhere.</div>
  <div class="body">Coordinate activities across departments. Easilyem-bed workflow in any application.</div>
  <div class="body">Create one applicationto access all your business operationsfast.</div>
</div>

<footer class="site-footer abs">
  <div class="footer-col news abs">
    <h3>Latest News</h3>
    <h4>Lorem ipsum dolor sit amet consectetur adipis</h4>
    <time>April 21, 2013</time>
    <p>Lorem ipsum dolor sit amet, consectetur adipiscing elit. Ut sit amet metus ut lorem pharetra...<a>[Read More]</a></p>
    <h4 style="margin-top:14px">Pellentesque congue purus vitae ante</h4>
    <time>April 21, 2013</time>
    <p>Lorem ipsum dolor sit amet, consectetur adipiscing elit. Ut sit amet metus ut lorem phaultrices...<a>[Read More]</a></p>
  </div>

  <div class="footer-col center abs">
    <div class="brand"><span class="brand-mark"></span><span class="brand-name">Emberlift</span></div>
    <div class="info"><svg width="12" height="14" viewBox="0 0 12 14"><path d="M6 0a5 5 0 0 1 5 5c0 4-5 9-5 9S1 9 1 5a5 5 0 0 1 5-5z" fill="#fff"/><circle cx="6" cy="5" r="2" fill="#0a5fa8"/></svg><span>4180 Larkspur Ln, Suite 112<br>Halden, MD 20910</span></div>
    <div class="info"><svg width="14" height="12" viewBox="0 0 14 12"><path d="M1 4c0-2 3-3 6-3s6 1 6 3v1h-3V3.5H4V5H1z M3 6h8l1 5H2z" fill="#fff"/></svg><span>+1 55 501 0199</span></div>
    <div class="info"><svg width="14" height="10" viewBox="0 0 14 10"><rect width="14" height="10" fill="#fff"/><path d="M0 0l7 5 7-5" fill="none" stroke="#0a5fa8"/></svg><span>sales@emberlift.net</span></div>
    <div class="socials"><span></span><span></span></div>
  </div>

  <div class="footer-col contact abs">
    <h3>Contact Us</h3>
    <div class="row2"><div class="field">First Name</div><div class="field">Last Name</div></div>
    <div class="row2"><div class="field">Email</div><div class="field">Phone</div></div>
    <div class="field msg">Enter Your Message</div>
    <div class="submit">Submit</div>
  </div>

  <div class="footer-bar abs">
    <p class="links abs">Home &nbsp;|&nbsp; Platform &nbsp;|&nbsp; Services &nbsp;|&nbsp; Blog &nbsp;|&nbsp; About Us</p>
    <p class="copy abs">Copyright © 2013 Emberlift. All Rights Reserved.</p>
  </div>
</footer>

</body>
</html>
```